Business Cards and Stationery for Borvexa engineering company.
Borvexa
Business Cards and Stationery for Borvexa engineering company. - Engineering
Creative Brief
Simple
Delgado Tarvin
Varnesk Region, Varnesk-on-Tal, st. Korvell, 283/7 office 42
tarvindelgado@mailbrook.example
logo on different backgrounds

```html
<!DOCTYPE html>
<html lang="en">
<head>
<meta charset="utf-8">
<title>Borvexa business card</title>
<link rel="stylesheet" href="https://fonts.googleapis.com/css2?family=Open+Sans:wght@400;600;700;800&display=swap">
<style>
  :root {
    --page-bg: #e9ebee;
    --card-white: #ffffff;
    --card-shade: #f1f2f4;
    --brand-blue: #1d8fd6;
    --band-light: #2aa3e6;
    --band-dark: #1373bd;
    --tab-light: #f4f6f8;
    --tab-dark: #c9ced4;
    --text-white: #ffffff;
  }
  * { margin: 0; padding: 0; box-sizing: border-box; }
  html, body {
    width: 1200px; height: 900px; overflow: hidden;
    background: var(--page-bg);
    font-family: "Open Sans", Arial, sans-serif;
  }
  .card {
    position: absolute; left: 180px; top: 210px;
    width: 840px; height: 480px;
    background: linear-gradient(180deg, var(--card-white) 0%, var(--card-shade) 100%);
    box-shadow: 0 10px 30px rgba(0,0,0,0.18);
    overflow: hidden;
  }
  .brand {
    position: absolute; left: 0; right: 0; top: 70px;
    display: flex; align-items: center; justify-content: center; gap: 18px;
  }
  .brand-dot {
    width: 70px; height: 70px; border-radius: 50%;
    background: var(--brand-blue);
  }
  .brand-name {
    font-weight: 800; font-size: 62px; letter-spacing: 0.5px;
    color: var(--brand-blue); line-height: 1;
  }
  .band {
    position: absolute; left: 0; right: 0; top: 212px; height: 200px;
    background: linear-gradient(90deg, var(--band-light) 0%, var(--brand-blue) 50%, var(--band-dark) 100%);
  }
  .name-tab {
    position: absolute; left: 0; top: 262px;
    width: 36px; height: 70px;
    background: linear-gradient(90deg, var(--tab-dark), var(--tab-light));
    border-radius: 0 6px 6px 0;
  }
  .holder-name {
    position: absolute; left: 50px; top: 282px;
    font-weight: 700; font-size: 22px; color: var(--text-white);
  }
  .contacts {
    position: absolute; left: 468px; top: 232px; width: 350px;
    list-style: none; color: var(--text-white);
    font-size: 17px; line-height: 1.45;
  }
  .contacts li { display: flex; gap: 10px; margin-bottom: 4px; }
  .contacts svg { flex: 0 0 18px; width: 18px; height: 18px; margin-top: 3px; }
</style>
</head>
<body>
  <main class="card">
    <div class="brand">
      <span class="brand-dot"></span>
      <span class="brand-name">Borvexa</span>
    </div>
    <div class="band"></div>
    <div class="name-tab"></div>
    <p class="holder-name">Delgado Tarvin</p>
    <ul class="contacts">
      <li>
        <svg viewBox="0 0 18 18"><circle cx="9" cy="9" r="9" fill="#fff"/><path d="M4.5 9.5 9 5.2l4.5 4.3h-1.3V13H5.8V9.5z" fill="#1d8fd6"/></svg>
        <span>Varnesk Region, Varnesk-on-Tal, st. Korvell, 283/7 office 42</span>
      </li>
      <li>
        <svg viewBox="0 0 18 18"><circle cx="9" cy="9" r="9" fill="#fff"/><rect x="6.2" y="4" width="5.6" height="10" rx="1" fill="#1d8fd6"/></svg>
        <span>89160473812</span>
      </li>
      <li>
        <svg viewBox="0 0 18 18"><circle cx="9" cy="9" r="9" fill="#fff"/><rect x="4.5" y="5.8" width="9" height="6.4" fill="#1d8fd6"/><path d="M4.5 5.8 9 9.4l4.5-3.6" stroke="#fff" stroke-width="0.9" fill="none"/></svg>
        <span>tarvindelgado@mailbrook.example</span>
      </li>
      <li>
        <svg viewBox="0 0 18 18"><circle cx="9" cy="9" r="9" fill="#fff"/><circle cx="9" cy="9" r="4.6" fill="none" stroke="#1d8fd6" stroke-width="1.2"/><path d="M4.4 9h9.2M9 4.4c-2.2 2.6-2.2 6.6 0 9.2M9 4.4c2.2 2.6 2.2 6.6 0 9.2" stroke="#1d8fd6" stroke-width="1" fill="none"/></svg>
        <span>www.borvexa.example</span>
      </li>
    </ul>
  </main>
</body>
</html>
```